Coffee label for coffee brand - Kiln Lane coffee

We want someone to design a label for packaging of a coffee line. The design will then be printed on stickers.

It is called Kiln Lane Coffee (logo enclosed) I want to incorporate a streetscape and the idea is that with every different coffee it will be a different colour (we have 6 varieties at the moment) with a black background. It needs to have a modern feel.

It needs to have a blank area towards the bottom for the type of coffee which we will print later on)

text to include

'Roasting exceptional coffee'

Target Market(s)

Coffee drinkers - modern feel

Font styles to use
Sans Serif

Colors
f78f20
9bcb3b
33a6d7
b768aa

Requirements
Must have
• the logo incorporated
• Space for coffee variety
• Quote' Roasting exceptional coffee'
Nice to have
• Streetscape theme incorporated - bright colour varieties (would love metallic) (on black background)

```html
<!DOCTYPE html>
<html lang="en">
<head>
<meta charset="utf-8">
<title>Kiln Lane Coffee – label range</title>
<link rel="stylesheet" href="https://fonts.googleapis.com/css2?family=Francois+One&family=Josefin+Sans:wght@300;600&display=swap">
<style>
  :root {
    --backdrop: #e6e7e9;
    --pouch-black: #1c1a1d;
    --tab-grey: #33393d;
    --ink-white: #ffffff;
    --street-light: #d9d9d9;
    --street-dark: #4a4a4a;
    --variety-yellow: #f3c623;
    --variety-yellow-tint: #b07a3e;
    --variety-blue: #33b5e5;
    --variety-blue-tint: #2fa9a9;
  }
  * { box-sizing: border-box; margin: 0; padding: 0; }
  html, body { width: 1200px; height: 999px; overflow: hidden; }
  body {
    background: var(--backdrop);
    font-family: "Josefin Sans", sans-serif;
    position: relative;
  }
  .label {
    position: absolute;
    top: 60px;
    width: 520px;
    height: 880px;
    background: var(--pouch-black);
  }
  .label--yellow { left: 50px; --accent: var(--variety-yellow); --tint: var(--variety-yellow-tint); }
  .label--blue { left: 630px; --accent: var(--variety-blue); --tint: var(--variety-blue-tint); }

  .streetscape {
    position: absolute;
    left: 30px; top: 170px;
    width: 460px; height: 520px;
    display: block;
  }
  .hang-tab {
    position: absolute;
    left: 130px; top: 20px;
    width: 260px; height: 400px;
    background: var(--tab-grey);
    display: flex;
    flex-direction: column;
    align-items: center;
  }
  .hang-slot {
    margin-top: 24px;
    width: 170px; height: 26px;
    border-radius: 13px;
    background: var(--backdrop);
  }
  .brand-name {
    margin-top: auto;
    margin-bottom: 70px;
    display: flex;
    align-items: center;
    gap: 12px;
    color: var(--ink-white);
    font-weight: 600;
    font-size: 30px;
    line-height: 1.1;
    text-align: left;
  }
  .brand-mark {
    width: 18px; height: 18px;
    background: var(--ink-white);
    flex: none;
  }
  .headline {
    position: absolute;
    left: 70px; top: 500px;
    font-family: "Francois One", sans-serif;
    font-size: 46px;
    line-height: 1.08;
    letter-spacing: 2px;
    text-transform: uppercase;
    color: var(--ink-white);
  }
  .variety-band {
    position: absolute;
    left: 30px; top: 690px;
    width: 460px; height: 115px;
    background: var(--accent);
    color: var(--ink-white);
    font-weight: 300;
    font-size: 30px;
    line-height: 1.45;
    text-align: center;
    display: flex;
    flex-direction: column;
    justify-content: center;
  }
</style>
</head>
<body>

  <section class="label label--yellow">
    <svg class="streetscape" viewBox="0 0 460 520" role="img" aria-label="City streetscape photograph, left half tinted amber, right half black and white">
      <defs>
        <linearGradient id="street-grey-a" x1="0" y1="0" x2="1" y2="1">
          <stop offset="0" stop-color="#555"/><stop offset="1" stop-color="#d4d4d4"/>
        </linearGradient>
      </defs>
      <rect width="460" height="520" fill="url(#street-grey-a)"/>
      <polygon points="0,0 200,0 420,520 0,520" fill="var(--tint)" opacity="0.85"/>
    </svg>
    <div class="hang-tab">
      <span class="hang-slot"></span>
      <p class="brand-name"><span class="brand-mark"></span>Kiln Lane<br>Coffee</p>
    </div>
    <h1 class="headline">Roasting<br>exceptional<br>coffee</h1>
    <div class="variety-band">
      <p>coffee name</p>
      <p>type &amp; strenght</p>
    </div>
  </section>

  <section class="label label--blue">
    <svg class="streetscape" viewBox="0 0 460 520" role="img" aria-label="City streetscape photograph, left half tinted teal, right half black and white">
      <defs>
        <linearGradient id="street-grey-b" x1="0" y1="0" x2="1" y2="1">
          <stop offset="0" stop-color="#555"/><stop offset="1" stop-color="#d4d4d4"/>
        </linearGradient>
      </defs>
      <rect width="460" height="520" fill="url(#street-grey-b)"/>
      <polygon points="0,0 200,0 420,520 0,520" fill="var(--tint)" opacity="0.85"/>
    </svg>
    <div class="hang-tab">
      <span class="hang-slot"></span>
      <p class="brand-name"><span class="brand-mark"></span>Kiln Lane<br>Coffee</p>
    </div>
    <h1 class="headline">Roasting<br>exceptional<br>coffee</h1>
    <div class="variety-band">
      <p>coffee name</p>
      <p>type &amp; strenght</p>
    </div>
  </section>

</body>
</html>
```